Wren's Hearth Support Business Card

Business card design
Font must be in Poppins Regular for Wren's Hearth Support
Safe Days Ahead font is Alex Brush

Colour must be Hex #910E2B
RGB 145-14-43
Pantone 7427 C
We want the card editable
On the front please include
Name eg Mavis Dunleavy
Position eg Clinical Care Manager
Phone number mobile 0473 856 342
Phone 08 7394 2650
Email : mavis@wrenshearthsupport.com.au
Address : Gullwing Cove, Coral Shire, 5291
Website : wrenshearthsupport.com.au
Contact us today to experience the warmth, respect and personal touch of Wren's Hearth Support.

Target Market(s)

35+

Industry/Entity Type

aged care / community

Contact Information for Business Card

see project description

Requirements
Must have
• Colours, logos and fonts as detailed and uploaded

```html
<!DOCTYPE html>
<html lang="en">
<head>
<meta charset="utf-8">
<title>Wren's Hearth Support – Business Card</title>
<link rel="stylesheet" href="https://fonts.googleapis.com/css2?family=Alex+Brush&family=Poppins:wght@400;500;700&display=swap">
<style>
  :root {
    --brand-red: #910E2B;
    --red-deep: #55000f;
    --red-mid: #7a0f24;
    --card-black: #050505;
    --ink-white: #ffffff;
    --faint-ring: rgba(255,255,255,0.06);
    --page-bg: #ece8e3;
  }
  * { box-sizing: border-box; margin: 0; padding: 0; }
  html, body { width: 1200px; height: 900px; overflow: hidden; }
  body {
    background: var(--page-bg);
    font-family: "Poppins", sans-serif;
    position: relative;
  }
  .card {
    position: absolute;
    width: 700px;
    height: 400px;
    overflow: hidden;
    box-shadow: 0 18px 40px rgba(0,0,0,0.25);
  }

  /* Back of card */
  .card-back {
    left: 70px; top: 50px;
    border-radius: 40px 0 40px 0;
    background: linear-gradient(120deg, var(--brand-red) 0%, var(--red-mid) 45%, var(--red-deep) 100%);
  }
  .card-back .emblem-ring {
    position: absolute;
    left: 60px; top: 130px;
    width: 330px; height: 330px;
    border-radius: 50%;
    border: 14px solid rgba(0,0,0,0.12);
    background: rgba(255,255,255,0.04);
  }
  .card-back .invitation {
    position: absolute;
    right: 50px; top: 48px;
    width: 360px;
    color: var(--ink-white);
    font-size: 17px;
    line-height: 1.55;
    text-align: center;
  }
  .card-back .invitation strong { font-weight: 700; }

  /* Front of card */
  .card-front {
    left: 430px; top: 460px;
    border-radius: 0 40px 0 40px;
    background: var(--card-black);
  }
  .card-front .emblem-ring {
    position: absolute;
    left: 90px; top: 110px;
    width: 330px; height: 330px;
    border-radius: 50%;
    border: 16px solid var(--faint-ring);
  }
  .contact-block {
    position: absolute;
    left: 42px; top: 60px;
    width: 340px;
  }
  .person-name {
    color: var(--brand-red);
    font-weight: 700;
    font-size: 21px;
    letter-spacing: 0.5px;
    text-transform: uppercase;
    line-height: 1.1;
  }
  .person-role {
    color: var(--ink-white);
    font-size: 15px;
    margin-top: 2px;
  }
  .contact-list {
    list-style: none;
    margin-top: 34px;
  }
  .contact-list li {
    display: flex;
    align-items: center;
    gap: 12px;
    color: var(--ink-white);
    font-size: 14.5px;
    line-height: 1;
    margin-bottom: 10px;
  }
  .contact-list svg { width: 14px; height: 14px; flex: none; }
  .divider {
    height: 1px;
    width: 300px;
    margin: 16px 0 14px 26px;
    background: linear-gradient(90deg, var(--brand-red), rgba(145,14,43,0.2));
  }
  .address {
    color: var(--ink-white);
    font-size: 14.5px;
    margin-left: 26px;
  }

  .brand-lockup {
    position: absolute;
    left: 392px; top: 140px;
    display: flex;
    align-items: center;
    gap: 14px;
  }
  .brand-mark {
    width: 62px; height: 62px;
    border-radius: 50%;
    border: 5px solid var(--brand-red);
    flex: none;
  }
  .brand-text {
    display: flex;
    flex-direction: column;
  }
  .brand-name {
    color: var(--brand-red);
    font-size: 28px;
    font-weight: 400;
    line-height: 1.05;
  }
  .brand-tagline {
    color: var(--brand-red);
    font-family: "Alex Brush", cursive;
    font-size: 26px;
    line-height: 1.2;
    margin-top: 6px;
    padding-left: 20px;
  }
</style>
</head>
<body>

  <section class="card card-back" aria-label="Business card back">
    <div class="emblem-ring"></div>
    <p class="invitation">Contact us today to experience the warmth, respect and personal touch of <strong>Wren's Hearth Support.</strong></p>
  </section>

  <section class="card card-front" aria-label="Business card front">
    <div class="emblem-ring"></div>

    <div class="contact-block">
      <h1 class="person-name">Mavis Dunleavy</h1>
      <p class="person-role">Clinical Care Manager</p>

      <ul class="contact-list">
        <li>
          <svg viewBox="0 0 14 14" aria-hidden="true"><rect x="3.5" y="0.8" width="7" height="12.4" rx="1.4" fill="none" stroke="#910E2B" stroke-width="1.2"/><line x1="6" y1="11" x2="8" y2="11" stroke="#910E2B" stroke-width="1.2"/></svg>
          0473 856 342
        </li>
        <li>
          <svg viewBox="0 0 14 14" aria-hidden="true"><path d="M3 1.2 L5.2 3.8 L4 5.4 Q5.4 8.4 8.6 10 L10.2 8.8 L12.8 11 L11.4 12.8 Q5.6 12.4 1.2 2.6 Z" fill="#910E2B"/></svg>
          08 7394 2650
        </li>
        <li>
          <svg viewBox="0 0 14 14" aria-hidden="true"><rect x="0.8" y="2.8" width="12.4" height="8.4" rx="1" fill="#910E2B"/><path d="M1.2 3.4 L7 8 L12.8 3.4" fill="none" stroke="#050505" stroke-width="1.1"/></svg>
          mavis@wrenshearthsupport.com.au
        </li>
        <li>
          <svg viewBox="0 0 14 14" aria-hidden="true"><g fill="none" stroke="#910E2B" stroke-width="1.1"><circle cx="7" cy="7" r="6"/><ellipse cx="7" cy="7" rx="2.6" ry="6"/><line x1="1" y1="7" x2="13" y2="7"/></g></svg>
          wrenshearthsupport.com.au
        </li>
      </ul>

      <div class="divider"></div>
      <p class="address">Gullwing Cove, Coral Shire, 5291</p>
    </div>

    <div class="brand-lockup">
      <span class="brand-mark"></span>
      <div class="brand-text">
        <span class="brand-name">Wren's<br>Hearth Support</span>
        <span class="brand-tagline">Safe Days Ahead</span>
      </div>
    </div>
  </section>

</body>
</html>
```